Web Design Project - Beachwear Affiliate Website needs an eyedropping look!

Hello,
I need a website design that incorporates a logo design as well for an affiliate site that features beachwear including swimwear, coverups, hats, bags, etc. I want it to have the look and feel of an ecommerce site but without the shopping cart so when the visitor gets to the purchase/buy button, they will be sent to the partner via affiliate link in a new window. This is a site targeting women's beachwear so I'm looking for a soft color palette.
LOGO: Looking for a beautiful text based logo with elegant fonts. The Site Logo should read "Tidelane Outfitters" with possibly some sort of break element between the two words. Possibly two different colors for each word. Please no beach type elements such as sun, umbrella, etc. Just nice and clean.
This requires 4 distinct page levels/designs. All pages should have navigation to the other categories without paging backwards.
Main Page - Large picture window in the top center. I would like this to be a slider rotating various pictures. 4 smaller picture spaces specials or products should be underneath the main picture. One should be designed in the style of the site with a text box reading "Weekly Specials".
Main Menu's for the following product categories: Home, Bikinis, One Piece Swimsuits, Modest Swimwear, Beach Cover Ups, Beach Hats & Bags, Specialty Swimwear, About Sizing) For Menu categories above that require subcategories, I'd like a mouseover effect to show the subcategories so users can bypass the subcategories page through direct navigation. Smaller links in the top right or bottom center for About Us, Contact, & Partners.
Subcategory Page - For Bikinis, Modest Swimwear, and Specialty Swimwear, I need a subcategory page offering image based sub-categories with text. The top of each of these pages should have space for text content. Please use filler text in your designs to get a sense for look. It can say anything or just be jibberish in your example. I will provide the subcategories in a separate uploaded file but as an example, Bikinis will have categories like String Bikinis, Brazilian Bikinis, G-string Bikini's etc. (Note Images should be sized to 200w x 312h pixels)
Category Page - This will be the main image gallery page for each category/subcategory. Images with ability to add pricing text underneath. Two buttons per image: More Info & Purchase. Purchase will take them to an external website utilizing affiliate links in a new window. More Info or clicking on the picture will take you to the product page. (Note images should be sized to 200w x 312h pixels
Product Page - Larger image sized to 420w x 629h with space for a product description to the right along with space to add sizing information as needed. Purchase button will take user to external website utilizing affiliate links in a new window.
Target Market(s)
Women 21-50 searching for Beachwear
Industry/Entity Type
Shopping
Requirements
Must have
- Please see details in the project description. Pages need to be able to be easily SEO'd and incorporate search engine friendly urls.
Simplicity in updating or adding product pages or additional categories is essential.
Social Network Integrated buttons for Quillo, Mingleboard, and Vantora Circle throughout the site.
Nice to have
- I'd really like to integrate a blog posting page so that I can add unique written content for the search engines.
Should not have
- Shopping cart/Ecommerce
Dark Color Palette

```html
<!DOCTYPE html>
<html lang="en">
<head>
<meta charset="utf-8">
<title>Tidelane Outfitters</title>
<link rel="stylesheet" href="https://fonts.googleapis.com/css2?family=Oswald:wght@400;500&family=PT+Sans:wght@400;700&family=Shadows+Into+Light&display=swap">
<style>
:root{
  --pink:#d4145a;
  --pink-dark:#b80d4b;
  --pink-soft:#f06aa0;
  --blush:#fbf1f3;
  --ink:#333;
  --muted:#777;
  --line:#e4e4e4;
  --panel:#f2f2f2;
  --footer:#2e2e2e;
  --footer-base:#1d1d1d;
  --white:#fff;
}
*{box-sizing:border-box;margin:0;padding:0}
html,body{width:697px;height:1200px;overflow:hidden}
body{position:relative;background:var(--white);font-family:"PT Sans",sans-serif;color:var(--ink);font-size:9px}
.abs{position:absolute}
.hero-band{left:0;top:0;width:697px;height:390px;background:linear-gradient(180deg,#fff 0%,var(--blush) 100%)}
.brand{left:28px;top:22px;font-family:"Oswald",sans-serif;font-weight:500;font-size:22px;color:var(--pink);letter-spacing:.5px}
.search{left:490px;top:32px;width:176px;height:21px;border:1px solid #d6d6d6;background:#f7f7f7;font-size:7px;color:#999;padding:6px 7px;font-style:italic}
.search svg{position:absolute;right:5px;top:4px}
.main-nav{left:24px;top:66px;width:648px;height:44px;border-radius:4px;background:linear-gradient(180deg,#e23a78 0%,var(--pink) 55%,var(--pink-dark) 100%);display:flex;box-shadow:0 1px 2px rgba(0,0,0,.2)}
.main-nav a{display:flex;align-items:center;padding:0 11px;font-family:"Oswald",sans-serif;font-size:10.5px;line-height:1.25;color:var(--white);text-decoration:none;border-right:1px solid rgba(255,255,255,.25);text-transform:uppercase}
.main-nav a:last-child{border-right:none}
.slider{left:24px;top:114px;width:650px;height:260px;background:var(--white);box-shadow:0 0 3px rgba(0,0,0,.15)}
.slide-photo{left:27px;top:118px;width:642px;height:252px;background:linear-gradient(100deg,#2c7f9a 0%,#3fa2b4 45%,#c89a7c 75%,#6f5a4e 100%)}
.slide-caption{left:27px;top:284px;width:285px;height:86px;background:rgba(255,255,255,.92);border-top-right-radius:14px}
.slide-caption .cap-name{position:absolute;left:18px;top:14px;font-family:"Oswald",sans-serif;font-size:18px;font-weight:500;color:var(--ink)}
.slide-caption .cap-tag{position:absolute;left:20px;top:45px;font-family:"Shadows Into Light",cursive;font-size:16px;color:#444}
.dots{left:622px;top:356px;display:flex;gap:3px}
.dots span{width:5px;height:5px;border-radius:50%;background:var(--white)}
.section-title{font-family:"Oswald",sans-serif;font-weight:500;color:var(--pink);font-size:14px}
.specials-title{left:27px;top:405px}
.thumb{top:430px;width:156px;height:119px;background:var(--white);box-shadow:0 0 3px rgba(0,0,0,.18);padding:3px}
.thumb div{width:100%;height:100%}
.side-box{left:26px;width:172px;border:1px solid var(--line);background:var(--white)}
.side-head{height:31px;padding:7px 10px;font-family:"Oswald",sans-serif;font-size:13px;color:#444;background:linear-gradient(180deg,#f7f7f7,#ebebeb)}
.best{top:571px;height:156px}
.best ul{list-style:none;padding:7px 0 0 20px}
.best li{font-size:8px;color:var(--muted);line-height:17.6px;position:relative;padding-left:10px}
.best li:before{content:"›";position:absolute;left:0;color:#bbb}
.blog{top:734px;height:279px}
.blog .side-head{background:linear-gradient(180deg,#f58bb4,var(--pink-soft));color:var(--white)}
.post{padding:10px 14px 0 14px;height:56px}
.post h4{font-weight:400;font-size:9.5px;color:#444;margin-bottom:2px}
.post p{font-size:7px;color:var(--muted);line-height:13px}
.welcome{left:216px;top:570px;width:450px}
.welcome h1{font-family:"Oswald",sans-serif;font-weight:500;font-size:16px;color:#2b2b2b;text-transform:uppercase}
.welcome h2{font-size:9.5px;font-weight:400;color:#333;margin:8px 0 6px}
.welcome p{font-size:7.4px;color:var(--muted);line-height:14px}
.divider{left:216px;top:683px;width:450px;height:1px;background:var(--line)}
.tile{width:214px;height:137px;background:var(--white);box-shadow:0 0 3px rgba(0,0,0,.18);padding:3px}
.tile .tile-photo{width:100%;height:131px}
.tile .tile-bar{position:absolute;left:3px;bottom:3px;right:3px;height:33px;background:rgba(25,25,25,.88);display:flex;justify-content:space-between;align-items:center}
.tile .tile-bar span{font-family:"Oswald",sans-serif;font-size:12px;color:var(--white);padding-left:14px;text-transform:uppercase}
.tile .tile-bar a{height:100%;width:62px;background:var(--pink);color:var(--white);font-family:"Oswald",sans-serif;font-size:11.5px;display:flex;align-items:center;justify-content:center;text-decoration:none}
.footer{left:0;top:1036px;width:697px;height:126px;background:var(--footer)}
.footer-col{top:1058px}
.footer-col h5{font-family:"Oswald",sans-serif;font-weight:400;font-size:11px;color:var(--white);margin-bottom:8px}
.footer-col li{list-style:none;font-size:8.5px;color:#e6e6e6;line-height:20px;padding-left:10px;position:relative}
.footer-col li:before{content:"";position:absolute;left:0;top:7px;border-left:4px solid #ddd;border-top:3px solid transparent;border-bottom:3px solid transparent}
.social li{padding-left:23px;line-height:22px}
.social li:before{left:0;top:3px;width:15px;height:15px;border:none;border-radius:50%;background:var(--white)}
.footer-base{left:0;top:1162px;width:697px;height:38px;background:var(--footer-base);color:#bbb;font-size:7.5px;padding:14px 33px}
</style>
</head>
<body>
<div class="abs hero-band"></div>

<header>
  <div class="abs brand">Tidelane Outfitters</div>
  <div class="abs search">Search here..
    <svg width="12" height="12" viewBox="0 0 12 12"><circle cx="5" cy="5" r="3.6" fill="none" stroke="#888" stroke-width="1.5"/><line x1="7.6" y1="7.6" x2="11" y2="11" stroke="#888" stroke-width="1.8"/></svg>
  </div>
  <nav class="abs main-nav">
    <a href="#" style="padding:0 18px">Home</a>
    <a href="#" style="padding:0 13px">Bikinis</a>
    <a href="#" style="padding:0 13px">One Piece<br>Swimsuits</a>
    <a href="#" style="padding:0 11px">Modest<br>Swimwear</a>
    <a href="#" style="padding:0 11px">Beach<br>Cover Ups</a>
    <a href="#" style="padding:0 8px">Beach<br>Hats &amp; Bags</a>
    <a href="#" style="padding:0 10px">Specialty<br>Swimwear</a>
    <a href="#" style="padding:0 8px">About Sizing</a>
    <a href="#" style="padding:0 8px">Contact</a>
  </nav>
</header>

<section>
  <div class="abs slider"></div>
  <div class="abs slide-photo" role="img" aria-label="Slider photo: woman in a patterned bikini on a boat railing by the sea"></div>
  <div class="abs slide-caption">
    <div class="cap-name">TIDELANE OUTFITTERS</div>
    <div class="cap-tag">We will be selling womens beachwear</div>
  </div>
  <div class="abs dots"><span></span><span></span><span></span><span></span></div>
</section>

<section>
  <h3 class="abs section-title specials-title">Weekly Specials</h3>
  <div class="abs thumb" style="left:26px"><div role="img" aria-label="Woman in a purple polka dot swimsuit on the beach" style="background:linear-gradient(180deg,#7fc1e0,#3a6fb0 60%,#e9d6bf)"></div></div>
  <div class="abs thumb" style="left:190px"><div role="img" aria-label="Woman in a black bikini against sky and waves" style="background:linear-gradient(180deg,#9fb9d6,#335d8c 65%,#1f3f66)"></div></div>
  <div class="abs thumb" style="left:353px"><div role="img" aria-label="Woman in a sun hat and patterned swimsuit on sand" style="background:linear-gradient(180deg,#cfe3ea,#e6ddd3 60%,#d9c8b4)"></div></div>
  <div class="abs thumb" style="left:517px"><div role="img" aria-label="Woman in a yellow bikini lying on the beach" style="background:linear-gradient(180deg,#a6d4e4,#e4d6bf 55%,#c89c7a)"></div></div>
</section>

<aside>
  <div class="abs side-box best">
    <div class="side-head">Best Selling</div>
    <ul>
      <li>dui viverra vestibulum.</li>
      <li>Suspendisse vulputate</li>
      <li>Aliquam dui</li>
      <li>Duis tincidunt lectus</li>
      <li>Nulla elementum</li>
      <li>Dui ut augue</li>
    </ul>
  </div>
  <div class="abs side-box blog">
    <div class="side-head">Recent Blog Post</div>
    <div class="post"><h4>Mauris vel lacus vitae</h4><p>Felis vestibulum volutpat. Etiam est nunc,<br>venenatis in, tristique eu, imperdiet</p></div>
    <div class="post"><h4>Duis non nunc</h4><p>Felis vestibulum volutpat. Etiam est nunc,<br>venenatis in, tristique eu, imperdiet</p></div>
    <div class="post"><h4>Duis non nunc</h4><p>Felis vestibulum volutpat. Etiam est nunc,<br>venenatis in, tristique eu, imperdiet</p></div>
    <div class="post"><h4>Vivamus sollicitudin</h4><p>Felis vestibulum volutpat. Etiam est nunc,<br>venenatis in, tristique eu, imperdiet</p></div>
  </div>
</aside>

<main>
  <div class="abs welcome">
    <h1>Welcome to our website mainpage..</h1>
    <h2>Duis tincidunt lectus quis dui viverra vestibulum.</h2>
    <p>Mauris vel lacus vitae felis vestibulum volutpat. Etiam est nunc, venenatis in, tristique eu, imperdiet ac, nisl. Cum sociis natoque penatibus et magnis dis parturient montes, nascetur ridiculus mus. In iaculis facilisis massa. Etiam eu urna. Sed porta. Suspendisse quam leo, molestie sed, luctus quis, feugiat in, pede. Fusce tellus. Sed metus augue, convallis et, vehicula ut, pulvinar eu, ante. Integer orci tellus, tristique vitae, consequat nec, porta vel, lectus. Nulla sit amet diam. Duis non nunc.</p>
  </div>
  <div class="abs divider"></div>

  <div class="abs tile" style="left:218px;top:703px">
    <div class="tile-photo" role="img" aria-label="Woman in a yellow and blue bikini by the sea" style="background:linear-gradient(180deg,#a9cfe6,#5e9cc4 60%,#3f6e93)"></div>
    <div class="tile-bar"><span>Bikinis</span><a href="#">BUY NOW</a></div>
  </div>
  <div class="abs tile" style="left:441px;top:703px">
    <div class="tile-photo" role="img" aria-label="Woman in a teal swimsuit sitting on rocks by the shore" style="background:linear-gradient(180deg,#8a6e5c,#d8c7b3 35%,#6fc1c9 75%,#3f9aa8)"></div>
    <div class="tile-bar"><span>Specialty Swimwear</span><a href="#">BUY NOW</a></div>
  </div>
  <div class="abs tile" style="left:220px;top:858px">
    <div class="tile-photo" role="img" aria-label="Woman in a turquoise swimsuit lying on white sand" style="background:linear-gradient(180deg,#bfe0ea,#5cc0c8 35%,#efe6d6 65%,#d9c6ae)"></div>
    <div class="tile-bar"><span>Modest Swimwear</span><a href="#">BUY NOW</a></div>
  </div>
  <div class="abs tile" style="left:444px;top:858px">
    <div class="tile-photo" role="img" aria-label="Striped beach chairs with a straw hat and bag" style="background:linear-gradient(180deg,#cfe9f1,#48b4c8 40%,#e9d9b8 70%,#c8a46e)"></div>
    <div class="tile-bar"><span>Beach Hats &amp; Bags</span><a href="#">BUY NOW</a></div>
  </div>
</main>

<footer>
  <div class="abs footer"></div>
  <div class="abs footer-col" style="left:38px"><h5>INFORMATION</h5><ul><li>Bikinis</li><li>One Piece Swimsuits</li><li>Modest Swimwear</li></ul></div>
  <div class="abs footer-col" style="left:173px"><h5>WHY CHOOSE US</h5><ul><li>Mauris vel lacus</li><li>Vitae felis vestibulum</li><li>Etiam est nunc</li></ul></div>
  <div class="abs footer-col" style="left:310px"><h5>BEACH WEAR</h5><ul><li>Mauris vel lacus</li><li>Vitae felis vestibulum</li><li>Etiam est nunc</li></ul></div>
  <div class="abs footer-col" style="left:441px"><h5>SUPPORT</h5><ul><li>Mauris vel lacus</li><li>Vitae felis vestibulum</li><li>Etiam est nunc</li></ul></div>
  <div class="abs footer-col social" style="left:561px"><h5>GET CONNECTED</h5><ul><li>Mingleboard</li><li>Quillo</li><li>Linkory</li></ul></div>
  <div class="abs footer-base">© 2012 Company Name. &nbsp;All right reserved. &nbsp;Term of Use</div>
</footer>
</body>
</html>
```